Tail Haven Pet Services ABN 31 640 975 208 needs a Postcard Design

Genuine pet lover offering a professional and highly personalised pet service. I will visit your home daily to care for your pet in their own environment. THE OTHER OPTION FOR WHEN YOU GO ON HOLIDAYS. Dog Holiday Service (includes but not limited to) Feed, Water, Walk, Love & Play. Clean Litter Trays, Hutches & Cages. Administer Medication as Directed. Water Pot Plants & Collec Mail. Individual Dog Walking (Permanent or Casual). REASONABLE RATES. Police Check & References available upon request. Contact MARGOT 0412 846 293

```html
<!DOCTYPE html>
<html lang="en">
<head>
<meta charset="utf-8">
<title>Tail Haven Pet Services – Postcard</title>
<link rel="stylesheet" href="https://fonts.googleapis.com/css2?family=Oswald:wght@300&family=Open+Sans:wght@300&family=Lato:wght@300;400&display=swap">
<style>
  :root {
    --backdrop: #a8a8a8;
    --card: #ffffff;
    --ink: #111111;
    --muted: #8a8a8a;
    --soft: #c4c4c4;
    --accent-red: #a8171b;
    --tick: #e8632a;
    --rule: #9a9a9a;
  }
  * { box-sizing: border-box; margin: 0; padding: 0; }
  html, body { width: 1200px; height: 1100px; overflow: hidden; }
  body { background: var(--backdrop); position: relative; font-family: "Lato", sans-serif; }

  .card { position: absolute; left: 293px; width: 660px; height: 511px; background: var(--card); overflow: hidden; }
  .card--front { top: 18px; }
  .card--back { top: 547px; }

  .hero-photo { position: absolute; inset: 0;
    background:
      radial-gradient(ellipse 260px 300px at 470px 260px, #c8954e 0%, #b57d3c 45%, rgba(181,125,60,0) 75%),
      linear-gradient(180deg, #3e5676 0%, #5c6f7e 30%, #6f8659 55%, #76746d 72%, #6a6b6b 100%);
  }
  .headline-panel { position: absolute; left: 0; top: 0; width: 660px; height: 511px; }
  .headline { position: absolute; left: 24px; top: 104px; width: 311px; text-align: center;
    font-family: "Oswald", sans-serif; font-weight: 300; font-size: 46px; line-height: 59px; color: var(--ink); letter-spacing: -1.5px; }
  .tagline { position: absolute; left: 24px; top: 338px; width: 311px; text-align: center;
    font-family: "Open Sans", sans-serif; font-weight: 300; font-size: 27px; color: var(--soft); white-space: nowrap; }
  .tagline-rule { position: absolute; top: 383px; height: 1px; background: #dcdcdc; }

  .intro { position: absolute; left: 20px; top: 16px; width: 296px; text-align: center; font-size: 15.5px; line-height: 20px; color: var(--ink); }
  .holiday-heading { position: absolute; left: 10px; top: 73px; width: 316px; text-align: center; font-weight: 400; font-size: 16.5px; line-height: 20px; color: var(--accent-red); }
  .service-list { position: absolute; left: 20px; top: 124px; width: 300px; list-style: none; }
  .service-list li { position: absolute; left: 0; width: 296px; padding-left: 32px; font-weight: 300; font-size: 14.3px; line-height: 18px; color: var(--muted); }
  .service-list svg { position: absolute; left: 0; top: 2px; }
  .contact { position: absolute; left: 27px; top: 384px; display: flex; align-items: center; gap: 9px;
    font-family: "Oswald", sans-serif; font-weight: 300; font-size: 24px; letter-spacing: -0.9px; color: var(--accent-red); white-space: nowrap; }
  .divider { position: absolute; left: 319px; top: 65px; width: 1px; height: 353px; background: var(--rule); }
  .stamp-box { position: absolute; left: 502px; top: 25px; width: 134px; height: 134px; border: 1px solid var(--rule); }
  .address-line { position: absolute; left: 346px; width: 269px; height: 1px; background: var(--rule); }
</style>
</head>
<body>
  <section class="card card--front">
    <div class="hero-photo" role="img" aria-label="Photo of a golden labrador lying on a rock with mountain trees behind"></div>
    <svg class="headline-panel" viewBox="0 0 660 511" aria-hidden="true">
      <polygon points="24,57 304,57 335,107 335,463 57,463 24,422" fill="#ffffff"/>
    </svg>
    <h1 class="headline">A<br>Professional and<br>Highly Personalised<br>Pet Service</h1>
    <p class="tagline">from a genuine pet lover</p>
    <span class="tagline-rule" style="left:28px;width:146px"></span>
    <span class="tagline-rule" style="left:182px;width:146px"></span>
  </section>

  <section class="card card--back">
    <p class="intro">I will visit your home daily to care for your pet in their own environment.</p>
    <h2 class="holiday-heading">THE OTHER OPTION FOR WHEN YOU GO ON HOLIDAYS.</h2>
    <ul class="service-list">
      <li style="top:0">
        <svg width="18" height="16" viewBox="0 0 18 16"><rect x="1" y="3" width="12" height="12" fill="none" stroke="var(--tick)" stroke-width="1.6"/><path d="M4 8l3 4 9-11" fill="none" stroke="var(--tick)" stroke-width="2.2"/></svg>
        Dog Holiday Service (includes but not limited to) Feed, Water, Walk, Love &amp; Play.</li>
      <li style="top:46px">
        <svg width="18" height="16" viewBox="0 0 18 16"><rect x="1" y="3" width="12" height="12" fill="none" stroke="var(--tick)" stroke-width="1.6"/><path d="M4 8l3 4 9-11" fill="none" stroke="var(--tick)" stroke-width="2.2"/></svg>
        Clean Litter Trays, Hutches &amp; Cages.</li>
      <li style="top:74px">
        <svg width="18" height="16" viewBox="0 0 18 16"><rect x="1" y="3" width="12" height="12" fill="none" stroke="var(--tick)" stroke-width="1.6"/><path d="M4 8l3 4 9-11" fill="none" stroke="var(--tick)" stroke-width="2.2"/></svg>
        Administer Medication as Directed.</li>
      <li style="top:104px">
        <svg width="18" height="16" viewBox="0 0 18 16"><rect x="1" y="3" width="12" height="12" fill="none" stroke="var(--tick)" stroke-width="1.6"/><path d="M4 8l3 4 9-11" fill="none" stroke="var(--tick)" stroke-width="2.2"/></svg>
        Water Pot Plants &amp; Collect Mail.</li>
      <li style="top:132px">
        <svg width="18" height="16" viewBox="0 0 18 16"><rect x="1" y="3" width="12" height="12" fill="none" stroke="var(--tick)" stroke-width="1.6"/><path d="M4 8l3 4 9-11" fill="none" stroke="var(--tick)" stroke-width="2.2"/></svg>
        Individual Dog Walking (Permanent or Casual).</li>
      <li style="top:181px">
        <svg width="18" height="16" viewBox="0 0 18 16"><rect x="1" y="3" width="12" height="12" fill="none" stroke="var(--tick)" stroke-width="1.6"/><path d="M4 8l3 4 9-11" fill="none" stroke="var(--tick)" stroke-width="2.2"/></svg>
        REASONABLE RATES.</li>
      <li style="top:211px">
        <svg width="18" height="16" viewBox="0 0 18 16"><rect x="1" y="3" width="12" height="12" fill="none" stroke="var(--tick)" stroke-width="1.6"/><path d="M4 8l3 4 9-11" fill="none" stroke="var(--tick)" stroke-width="2.2"/></svg>
        Police Check &amp; References available upon request.</li>
    </ul>
    <p class="contact">
      <svg width="22" height="22" viewBox="0 0 22 22" aria-hidden="true"><circle cx="11" cy="11" r="10" fill="none" stroke="var(--muted)" stroke-width="1.4"/><path d="M8 6c-1.5 1-1.5 3 0 6s3.5 4.5 5.5 4l1-1.5-2-1.5-1 1c-1-.5-2.5-2.5-2.8-3.5l1-.8-1-2.2z" fill="none" stroke="var(--muted)" stroke-width="1.2"/></svg>
      Contact MARGOT 0412 846 293
    </p>
    <span class="divider"></span>
    <div class="stamp-box"></div>
    <span class="address-line" style="top:244px"></span>
    <span class="address-line" style="top:276px"></span>
    <span class="address-line" style="top:308px"></span>
    <span class="address-line" style="top:340px"></span>
    <span class="address-line" style="top:372px"></span>
  </section>
</body>
</html>
```